KVPLAX25

We want to make a full page advertisement that will be published in The Halvard magazine. It needs to be 8” x 10.75” high resolution. Our intention is to feature our upcoming attendance at KV-PLAX conference in Saratoga Springs, NY in April. More information about the show can be found at https://www.kv-plax.org/brenmoor-kv-plax-2025/. We want to showcase our rapid expansion and need for good quality people to join our team in the Northeast United States.

```html
<!DOCTYPE html>
<html lang="en">
<head>
<meta charset="utf-8">
<title>KV-PLAX 2025 Conference</title>
<link rel="stylesheet" href="https://fonts.googleapis.com/css2?family=League+Gothic&family=Poppins:wght@400;500;600;700;800&display=swap">
<style>
  :root {
    --page-bg: #d6d6d6;
    --ink: #0b0b0b;
    --red: #ef2a38;
    --red-soft: rgba(239, 42, 56, 0.82);
    --cyan: #29b6e6;
    --cyan-deep: #1a8fc4;
    --white: #f4f4f4;
    --muted: #d9d9d9;
  }
  * { margin: 0; padding: 0; box-sizing: border-box; }
  html, body { width: 910px; height: 1200px; overflow: hidden; }
  body { background: var(--page-bg); font-family: "Poppins", sans-serif; color: var(--white); position: relative; }

  .flyer {
    position: absolute; left: 73px; top: 86px; width: 766px; height: 1028px;
    background: var(--ink); overflow: hidden;
    box-shadow: 0 6px 18px rgba(0,0,0,0.25);
  }

  .hero-photo {
    position: absolute; left: 0; top: 0; width: 560px; height: 446px;
    background:
      linear-gradient(90deg, rgba(11,11,11,0) 60%, var(--ink) 100%),
      linear-gradient(180deg, #2aa6f0 0%, #5ec0f5 38%, #3f6b36 52%, #7b2b2b 72%, #c8323a 86%, #2b2b2b 100%);
  }
  .hero-arc { position: absolute; left: 0; top: 0; width: 560px; height: 446px; }

  .site-photo {
    position: absolute; left: 0; top: 680px; width: 766px; height: 348px;
    background: linear-gradient(180deg, var(--ink) 0%, #262626 30%, #1c1c1c 70%, #111 100%);
  }

  .side-photo {
    position: absolute; left: 539px; width: 189px; height: 173px;
    border: 3px solid var(--cyan); border-radius: 26px;
  }
  .side-photo--rig { top: 73px; background: linear-gradient(160deg, #8aa36a 0%, #b59a5a 45%, #c9a23a 75%, #5a4a2a 100%); }
  .side-photo--trench { top: 255px; background: linear-gradient(150deg, #b89878 0%, #d8c2a4 45%, #6b6058 75%, #c9b293 100%); }
  .side-photo--field { top: 440px; background: linear-gradient(180deg, #a9c8e4 0%, #d8e4ee 22%, #6b6a3c 42%, #7c8a4a 62%, #8a6a4c 82%, #5c4836 100%); }

  .condensed { font-family: "League Gothic", sans-serif; }

  .title { position: absolute; left: 79px; top: 452px; width: 294px; height: 144px; }
  .title svg { display: block; width: 294px; height: 144px; overflow: visible; }
  .title text { fill: var(--muted); font-size: 196px; }

  .title__year {
    position: absolute; left: 384px; top: 452px;
    font-family: "Poppins", sans-serif; font-weight: 800; font-size: 92px; line-height: 72px;
    color: var(--red); letter-spacing: -2px;
  }

  .band {
    position: absolute; left: 81px; top: 611px; width: 410px; height: 61px;
    background: var(--red); color: var(--white);
    font-weight: 800; font-size: 52px; line-height: 61px; text-align: center; letter-spacing: 0.5px;
  }

  .venue {
    position: absolute; left: 82px; top: 684px; display: flex; align-items: center; gap: 14px;
    font-weight: 600; font-size: 29px; color: var(--white); white-space: nowrap;
  }
  .venue svg { width: 20px; height: 28px; }

  .dates { position: absolute; left: 78px; top: 768px; width: 86px; height: 112px; }
  .dates svg { display: block; width: 86px; height: 112px; overflow: visible; }
  .dates__month { fill: var(--muted); font-size: 68px; }
  .dates__range { fill: var(--red); font-size: 72px; }

  .schedule { position: absolute; left: 177px; top: 764px; width: 220px; }
  .schedule__heading { font-weight: 600; font-size: 14px; color: var(--white); line-height: 18px; white-space: nowrap; }
  .schedule__row { display: flex; align-items: center; height: 21px; margin-top: 2px; margin-bottom: 4px; }
  .chip-month {
    height: 21px; width: 44px; display: flex; align-items: center; justify-content: center;
    background: linear-gradient(90deg, var(--cyan-deep), var(--cyan));
    color: #0d2b3a; font-weight: 700; font-size: 12.5px;
  }
  .chip-day {
    height: 21px; width: 28px; display: flex; align-items: center; justify-content: center;
    border: 1.5px solid var(--cyan); border-radius: 0 5px 5px 0; background: var(--ink);
    font-weight: 700; font-size: 13px; color: var(--white);
  }
  .schedule__day { margin-left: 8px; font-size: 14px; color: var(--white); white-space: nowrap; }
  .schedule__rule { height: 1px; width: 215px; background: #6b6b6b; margin: 3px 0 5px; }

  .highlights { position: absolute; left: 489px; top: 738px; width: 223px; }
  .highlights__label {
    position: relative; height: 35px; background: var(--ink);
    color: var(--red); font-weight: 500; font-size: 12.5px; letter-spacing: 1.5px; line-height: 35px; padding-left: 19px;
  }
  .highlights__label::after {
    content: ""; position: absolute; left: 42px; bottom: -8px;
    border-left: 8px solid transparent; border-right: 8px solid transparent; border-top: 8px solid var(--ink);
  }
  .highlights__list {
    list-style: none; height: 122px; padding: 13px 0 0 19px;
    background: linear-gradient(180deg, rgba(31,160,214,0.95), rgba(26,143,196,0.9));
  }
  .highlights__list li { display: flex; align-items: center; gap: 10px; height: 24px; font-size: 14px; color: var(--white); }
  .highlights__list svg { width: 15px; height: 15px; }

  .footer { position: absolute; left: 0; top: 920px; width: 766px; height: 70px; }
  .brand { position: absolute; left: 88px; top: 8px; display: flex; align-items: center; gap: 8px; }
  .brand__dot { width: 34px; height: 34px; border-radius: 50%; background: var(--cyan); }
  .brand__name { font-weight: 700; font-size: 16px; line-height: 1.05; color: var(--red); }
  .footer__item { position: absolute; top: 22px; font-size: 13.5px; color: var(--white); line-height: 17px; }
  .footer__item--contact { left: 267px; }
  .footer__item--web { left: 433px; }
  .footer__item--social { left: 614px; }
  .footer__value { display: flex; align-items: center; gap: 4px; white-space: nowrap; }
  .footer__value svg { width: 10px; height: 10px; }
  .social-dots { display: flex; gap: 3px; margin-top: 3px; }
  .social-dots span { width: 11px; height: 11px; border-radius: 50%; background: var(--red); }
</style>
</head>
<body>
<main class="flyer">
  <div class="hero-photo" role="img" aria-label="Two red geothermal drilling trucks with raised masts on a job site under blue sky"></div>
  <svg class="hero-arc" viewBox="0 0 560 446" aria-hidden="true">
    <path d="M379,0 L485,0 Q476,330 0,446 L0,398 Q338,318 379,0 Z" fill="var(--red-soft)"/>
  </svg>

  <div class="site-photo" role="img" aria-label="Faint dark view of a drilling site with rigs and equipment"></div>

  <div class="side-photo side-photo--rig" role="img" aria-label="Crew member in safety vest working beside a yellow drilling rig"></div>
  <div class="side-photo side-photo--trench" role="img" aria-label="Trench with rows of black geothermal loop pipes in sandy soil"></div>
  <div class="side-photo side-photo--field" role="img" aria-label="Several drill rigs working in an open field with trees behind"></div>

  <h1 class="title">
    <svg viewBox="0 0 294 144" aria-label="KV-PLAX">
      <text class="condensed" x="0" y="142" textLength="294" lengthAdjust="spacingAndGlyphs">KV-PLAX</text>
    </svg>
  </h1>
  <div class="title__year">20<br>25</div>

  <div class="band">CONFERENCE</div>

  <p class="venue">
    <svg viewBox="0 0 20 28" aria-hidden="true"><path d="M10 0C4.5 0 0 4.4 0 9.8 0 17 10 28 10 28s10-11 10-18.2C20 4.4 15.5 0 10 0zm0 13.5a3.7 3.7 0 1 1 0-7.4 3.7 3.7 0 0 1 0 7.4z" fill="var(--cyan)"/></svg>
    Brenmoor Grand Hotel &amp; Civic Center
  </p>

  <div class="dates">
    <svg viewBox="0 0 86 112" aria-label="April 22-24">
      <text class="condensed dates__month" x="0" y="50" textLength="84" lengthAdjust="spacingAndGlyphs">APRIL</text>
      <text class="condensed dates__range" x="0" y="110" textLength="79" lengthAdjust="spacingAndGlyphs">22-24</text>
    </svg>
  </div>

  <div class="schedule">
    <p class="schedule__heading">PRE CONFERENCE ACTIVITIES</p>
    <div class="schedule__row"><span class="chip-month">APRIL</span><span class="chip-day">22</span><span class="schedule__day">TUESDAY, EARTH DAY</span></div>
    <div class="schedule__rule"></div>
    <p class="schedule__heading">KV-PLAX 2025</p>
    <div class="schedule__row"><span class="chip-month">APRIL</span><span class="chip-day">23</span><span class="schedule__day">WEDNESDAY</span></div>
    <div class="schedule__row"><span class="chip-month">APRIL</span><span class="chip-day">24</span><span class="schedule__day">THURSDAY</span></div>
  </div>

  <section class="highlights">
    <p class="highlights__label">TWO FULL DAYS OF</p>
    <ul class="highlights__list">
      <li><svg viewBox="0 0 16 16" aria-hidden="true"><path d="M2 4h12v9H2zM8 4v9M5 2h6" fill="none" stroke="#e9f6fc" stroke-width="1.2"/></svg>Education</li>
      <li><svg viewBox="0 0 16 16" aria-hidden="true"><g fill="none" stroke="#e9f6fc" stroke-width="1.2"><circle cx="4" cy="4" r="2"/><circle cx="12" cy="4" r="2"/><circle cx="8" cy="12" r="2"/><path d="M5.5 5.5L7 10.5M10.5 5.5L9 10.5M6 4h4"/></g></svg>Exhibitor networking</li>
      <li><svg viewBox="0 0 16 16" aria-hidden="true"><g fill="none" stroke="#e9f6fc" stroke-width="1.2"><circle cx="8" cy="8" r="6.5"/><circle cx="8" cy="8" r="3.5"/></g></svg>Annual dinner</li>
      <li><svg viewBox="0 0 16 16" aria-hidden="true"><path d="M4 2h8v4a4 4 0 0 1-8 0zM8 10v3M5 14h6" fill="none" stroke="#e9f6fc" stroke-width="1.2"/></svg>Top Job Awards</li>
    </ul>
  </section>

  <footer class="footer">
    <div class="brand">
      <span class="brand__dot"></span>
      <span class="brand__name">Tarnwell<br>Geothermal</span>
    </div>
    <div class="footer__item footer__item--contact">
      <p>Contact us</p>
      <p class="footer__value"><svg viewBox="0 0 10 10" aria-hidden="true"><path d="M2 1l2 2-1 1.3a6 6 0 0 0 2.7 2.7L7 6l2 2-1.2 1.5C4.5 9.5.5 5.5.5 2.2z" fill="var(--red)"/></svg>1-800-555-0142</p>
    </div>
    <div class="footer__item footer__item--web">
      <p>Visit our website</p>
      <p class="footer__value"><svg viewBox="0 0 10 10" aria-hidden="true"><g fill="none" stroke="var(--red)" stroke-width="1"><circle cx="5" cy="5" r="4.3"/><path d="M.7 5h8.6M5 .7c-2 2.5-2 6.1 0 8.6M5 .7c2 2.5 2 6.1 0 8.6"/></g></svg>www.tarnwellgeo.com</p>
    </div>
    <div class="footer__item footer__item--social">
      <p>Follow us on</p>
      <div class="social-dots"><span></span><span></span><span></span></div>
    </div>
  </footer>
</main>
</body>
</html>
```